A flyer for future customers to get acquainted with our company

The flyer/card is intended for intermediaries. The purpose of this flyer is to introduce businesses to Dovrel.

It should convey: real estate and financing, with actual images. Various keywords describing what we do: project financing, temporary real estate financing, real estate financing, investment properties, transformations. We distinguish ourselves by being fast, flexible, and personal.

Please ensure the front has an attractive and inviting appearance, and leave space on the back for additional text.

Color codes: #E85B35 en #091E33

```html
<!DOCTYPE html>
<html lang="nl">
<head>
<meta charset="utf-8">
<title>Dovrel – kennismakingskaart</title>
<link rel="stylesheet" href="https://fonts.googleapis.com/css2?family=Poppins:wght@400;500;600;700;800&family=Oswald:wght@600&display=swap">
<style>
  :root{
    --orange:#E85B35;
    --navy:#091E33;
    --navy-band:#0d2a4d;
    --blue-tab:#1c4a86;
    --white:#ffffff;
    --paper:#e8e9eb;
    --stamp:#e3e3e4;
  }
  *{box-sizing:border-box;margin:0;padding:0}
  html,body{width:1200px;height:2400px;overflow:hidden}
  body{background:var(--paper);font-family:"Poppins",sans-serif;position:relative}
  .card{position:absolute;left:100px;width:1000px;height:667px;background:var(--white);overflow:hidden;box-shadow:0 10px 28px rgba(9,30,51,.22)}
  .card--front{top:483px}
  .card--back{top:1250px}
  .card svg.backdrop{position:absolute;inset:0}
  .abs{position:absolute}

  /* front */
  .brand{display:flex;align-items:center;gap:10px;font-family:"Poppins",sans-serif;font-weight:700;color:var(--navy);letter-spacing:-1px}
  .brand__dot{width:20px;height:20px;border-radius:50%;background:var(--orange)}
  .front-brand{left:35px;top:34px;font-size:66px;line-height:1}
  .kicker{left:35px;top:148px;font-size:22px;color:var(--navy);font-weight:400;letter-spacing:.3px}
  .headline{left:33px;top:160px;font-size:63px;font-weight:800;color:var(--orange);letter-spacing:.5px}
  .headline-sub{left:34px;top:226px;font-family:"Oswald",sans-serif;font-weight:600;font-size:40px;line-height:40px;color:var(--navy);letter-spacing:-.3px;transform:scaleX(.86);transform-origin:left;white-space:nowrap}
  .headline-end{left:34px;top:262px;font-size:33px;font-weight:800;color:var(--navy)}
  .since{left:35px;top:300px;font-size:15px;color:var(--navy);font-weight:500}
  .trait{top:444px;width:140px;text-align:center;color:var(--white);font-size:24px}
  .doing-title{left:35px;top:535px;font-size:27px;font-weight:700;color:var(--white)}
  .doing-title span,.accent{color:var(--orange)}
  .ticks{list-style:none;color:var(--white);font-size:16px}
  .ticks li{display:flex;align-items:center;gap:9px;height:31px}
  .tick{width:15px;height:15px;flex:none}
  .contact{color:var(--white);font-weight:600;font-size:20px;display:flex;align-items:center;gap:8px}
  .visit{left:572px;top:596px;width:389px;height:34px;display:flex;font-weight:600}
  .visit__label{width:118px;background:var(--blue-tab);color:var(--white);font-size:14px;letter-spacing:2px;display:flex;align-items:center;justify-content:center}
  .visit__url{flex:1;background:var(--orange);color:var(--white);font-size:22px;font-weight:700;letter-spacing:4px;display:flex;align-items:center;justify-content:center}

  /* back */
  .intro{left:35px;top:40px;width:440px;font-size:12.6px;line-height:15px;font-weight:700;color:var(--navy)}
  .service{color:var(--white)}
  .service--left{width:180px}
  .service--right{width:188px}
  .service h3{font-size:13px;font-weight:700;margin-bottom:3px;white-space:nowrap}
  .service p{font-size:11.2px;line-height:13px;font-weight:400}
  .perks-title{left:36px;top:386px;font-size:20px;font-weight:700;color:var(--white)}
  .perk{width:190px;color:var(--white);font-size:12.5px;line-height:15px;display:flex;gap:8px}
  .perk .tick{width:11px;height:11px;margin-top:2px}
  .back-phone{left:35px;top:555px;font-size:29px;font-weight:600;color:var(--white);display:flex;align-items:center;gap:10px}
  .back-url{left:35px;top:594px;font-size:26px;font-weight:700;letter-spacing:5px;color:var(--white)}
  .back-brand{left:539px;top:42px;font-size:58px;line-height:1}
</style>
</head>
<body>

<svg width="0" height="0" style="position:absolute">
  <defs>
    <symbol id="tick" viewBox="0 0 16 16"><circle cx="8" cy="8" r="8" fill="#E85B35"/><path d="M4.4 8.3l2.4 2.3 4.8-5" fill="none" stroke="#fff" stroke-width="1.9" stroke-linecap="round" stroke-linejoin="round"/></symbol>
    <symbol id="phone" viewBox="0 0 16 16"><circle cx="8" cy="8" r="8" fill="#E85B35"/><path d="M5.3 4.2c.5-.4 1-.3 1.2.2l.6 1.4c.2.4 0 .7-.3 1l-.4.3c.4.9 1.1 1.7 2 2.1l.4-.4c.3-.3.6-.4 1-.2l1.3.7c.4.2.5.8 0 1.2l-.6.5c-.6.5-1.600.5-2.700-.1-1.500-.8-2.800-2.100-3.400-3.600-.4-1-.3-1.900.3-2.500z" fill="#fff"/></symbol>
    <symbol id="mail" viewBox="0 0 16 16"><circle cx="8" cy="8" r="8" fill="#E85B35"/><rect x="4" y="5.2" width="8" height="5.6" rx=".6" fill="#fff"/><path d="M4.3 5.6L8 8.4l3.7-2.8" fill="none" stroke="#E85B35" stroke-width=".9"/></symbol>
    <symbol id="service-ring" viewBox="0 0 40 40"><circle cx="20" cy="20" r="18" fill="#fff" stroke="#091E33" stroke-width="2"/><circle cx="20" cy="20" r="14" fill="none" stroke="#E85B35" stroke-width="1.5"/></symbol>
  </defs>
</svg>

<!-- FRONT -->
<section class="card card--front" aria-label="Voorzijde">
  <svg class="backdrop" width="1000" height="667" viewBox="0 0 1000 667">
    <defs>
      <radialGradient id="photo-front" cx="0.45" cy="0.55" r="0.7">
        <stop offset="0" stop-color="#f0703f"/>
        <stop offset=".55" stop-color="#d9542a"/>
        <stop offset="1" stop-color="#6e2414"/>
      </radialGradient>
      <linearGradient id="band" x1="0" y1="0" x2="1" y2="0">
        <stop offset="0" stop-color="#0e2b4e"/>
        <stop offset="1" stop-color="#0a2240"/>
      </linearGradient>
    </defs>
    <rect x="0" y="391" width="1000" height="276" fill="url(#band)"/>
    <circle cx="712" cy="284" r="262" fill="var(--navy)"/>
    <circle cx="732" cy="266" r="248" fill="#fff"/>
    <circle cx="732" cy="266" r="230" fill="url(#photo-front)" role="img" aria-label="Foto: handen op een rekenmachine naast bankbiljetten, munten en een huismodel, in oranje tint"/>
    <line x1="33" y1="512" x2="513" y2="512" stroke="#6f86a6" stroke-width="1.3" stroke-dasharray="5 4"/>
    <line x1="152" y1="403" x2="152" y2="488" stroke="#6f86a6" stroke-width="1.2" stroke-dasharray="4 4"/>
    <line x1="310" y1="403" x2="310" y2="488" stroke="#6f86a6" stroke-width="1.2" stroke-dasharray="4 4"/>

    <g>
      <circle cx="81" cy="393" r="38" fill="#fff" stroke="var(--orange)" stroke-width="6"/>
      <circle cx="81" cy="396" r="18" fill="none" stroke="var(--navy)" stroke-width="2.4"/>
      <rect x="77" y="371" width="8" height="5" fill="var(--navy)"/>
      <path d="M81 396V385M81 396l7 5" stroke="var(--orange)" stroke-width="2.4" stroke-linecap="round"/>
    </g>
    <g>
      <circle cx="234" cy="393" r="38" fill="#fff" stroke="var(--orange)" stroke-width="6"/>
      <circle cx="234" cy="393" r="9" fill="none" stroke="var(--navy)" stroke-width="2.4"/>
      <circle cx="234" cy="393" r="14" fill="none" stroke="var(--navy)" stroke-width="3" stroke-dasharray="4 3"/>
      <path d="M214 384a22 22 0 0 1 34-8M254 402a22 22 0 0 1-34 8" fill="none" stroke="var(--orange)" stroke-width="2.4" stroke-linecap="round"/>
      <path d="M246 371l3 6-6 1M222 415l-3-6 6-1" fill="none" stroke="var(--orange)" stroke-width="2.2" stroke-linecap="round"/>
    </g>
    <g>
      <circle cx="401" cy="393" r="38" fill="#fff" stroke="var(--orange)" stroke-width="6"/>
      <rect x="386" y="375" width="26" height="34" rx="2" fill="none" stroke="var(--navy)" stroke-width="2.4"/>
      <circle cx="399" cy="385" r="4" fill="none" stroke="var(--orange)" stroke-width="2"/>
      <path d="M391 396h15M391 402h11" stroke="var(--navy)" stroke-width="2"/>
      <path d="M419 384l-12 18-2 5 4-3 12-18z" fill="var(--orange)"/>
    </g>
  </svg>

  <div class="abs brand front-brand">Dovrel<span class="brand__dot"></span></div>
  <p class="abs kicker">VLOTTE ACCEPTATIE</p>
  <h1 class="abs headline">CREATIEVE</h1>
  <p class="abs headline-sub">FINANCIERINGSOPLOSSINGEN</p>
  <p class="abs headline-end">EN MAATWERK</p>
  <p class="abs since">DAT IS WAT WE AL SINDS 2013 DOEN..</p>

  <p class="abs trait" style="left:11px">Snel</p>
  <p class="abs trait" style="left:164px">Flexibel</p>
  <p class="abs trait" style="left:315px;width:175px">Persoonlijk</p>

  <h2 class="abs doing-title"><span>Wat</span> Wij Doen..</h2>
  <ul class="abs ticks" style="left:35px;top:577px">
    <li><svg class="tick"><use href="#tick"/></svg>Projectfinancieringen</li>
    <li><svg class="tick"><use href="#tick"/></svg>Tijdelijke vastgoedfinancieringen</li>
  </ul>
  <ul class="abs ticks" style="left:340px;top:547px">
    <li><svg class="tick"><use href="#tick"/></svg>vastgoedfinancieringen</li>
    <li><svg class="tick"><use href="#tick"/></svg>Vastgoedbeleggingen</li>
    <li><svg class="tick"><use href="#tick"/></svg>Transformaties</li>
  </ul>

  <p class="abs contact" style="left:572px;top:558px"><svg class="tick"><use href="#phone"/></svg>(088) 415 62 90</p>
  <p class="abs contact" style="left:794px;top:556px;font-size:19px"><svg class="tick"><use href="#mail"/></svg>info@dovrel.nl</p>
  <div class="abs visit"><span class="visit__label">Visit Us At</span><span class="visit__url">www.dovrel.nl</span></div>
</section>

<!-- BACK -->
<section class="card card--back" aria-label="Achterzijde">
  <svg class="backdrop" width="1000" height="667" viewBox="0 0 1000 667">
    <defs>
      <linearGradient id="photo-back" x1="0" y1="0" x2="1" y2="1">
        <stop offset="0" stop-color="#e2643a"/>
        <stop offset=".5" stop-color="#8fa3bd"/>
        <stop offset="1" stop-color="#3d5678"/>
      </linearGradient>
    </defs>
    <rect x="0" y="0" width="517" height="374" fill="var(--orange)"/>
    <rect x="0" y="374" width="517" height="293" fill="var(--navy-band)"/>
    <circle cx="431" cy="667" r="154" fill="var(--orange)"/>
    <circle cx="452" cy="680" r="130" fill="url(#photo-back)" role="img" aria-label="Foto: zakelijke handen met een tablet aan een bureau"/>
    <line x1="35" y1="538" x2="300" y2="538" stroke="#6f86a6" stroke-width="1.2" stroke-dasharray="5 4"/>
    <rect x="813" y="35" width="150" height="172" fill="var(--stamp)"/>
    <g stroke="#2b3442" stroke-width="1.2">
      <line x1="602" y1="301" x2="963" y2="301"/>
      <line x1="602" y1="369" x2="963" y2="369"/>
      <line x1="602" y1="437" x2="963" y2="437"/>
    </g>
    <use href="#service-ring" x="35" y="99" width="34" height="34"/>
    <use href="#service-ring" x="271" y="99" width="34" height="34"/>
    <use href="#service-ring" x="35" y="179" width="34" height="34"/>
    <use href="#service-ring" x="271" y="179" width="34" height="34"/>
    <use href="#service-ring" x="35" y="257" width="34" height="34"/>
    <use href="#service-ring" x="271" y="262" width="34" height="34"/>
  </svg>

  <p class="abs intro">Iedere aanvraag bekijken we vanuit jouw ogen. We geven een eerlijk oordeel over je casus en geven binnen enkele dagen commitment, zodat jij je kunt focussen op je plannen.</p>

  <div class="abs service service--left" style="left:80px;top:103px"><h3>Handelsfinanciering</h3><p>Voor de vastgoedondernemer die onroerend goed aankoopt, renoveert en doorverkoopt.</p></div>
  <div class="abs service service--right" style="left:316px;top:103px"><h3>Transformatiefinanciering</h3><p>Wil je vastgoed aankopen en met een bestemmingswijziging waarde toevoegen?</p></div>
  <div class="abs service service--left" style="left:80px;top:183px"><h3>Bouwfinanciering</h3><p>Een pand kopen maar tijdelijk geen liquiditeit beschikbaar voor de aankoop of afbouw?</p></div>
  <div class="abs service service--right" style="left:316px;top:183px"><h3>Nieuwbouwfinanciering</h3><p>Van scratch af aan een beleggingspand of ander commercieel vastgoed realiseren?</p></div>
  <div class="abs service service--left" style="left:80px;top:261px"><h3>Beleggingsfinanciering</h3><p>De tijdelijke vastgoedfinanciering om te investeren in verhuurd en/of onverhuurd (commercieel) vastgoed.</p></div>
  <div class="abs service service--right" style="left:316px;top:266px"><h3>Stressfinanciering</h3><p>Voor ondernemers die na een faillissement een doorstart willen maken en/of een lopende bancaire schuld willen inlossen.</p></div>

  <h2 class="abs perks-title">Vastgoedfinanciering <span class="accent">voor ondernemers</span></h2>
  <p class="abs perk" style="left:35px;top:428px"><svg class="tick"><use href="#tick"/></svg><span>Voor het handelen in onroerend goed</span></p>
  <p class="abs perk" style="left:228px;top:428px;width:260px"><svg class="tick"><use href="#tick"/></svg><span>Het realiseren van een nieuwbouwcomplex of woningen</span></p>
  <p class="abs perk" style="left:35px;top:472px"><svg class="tick"><use href="#tick"/></svg><span>Voor transformatie van kantoorgebouwen naar appartementen</span></p>
  <p class="abs perk" style="left:228px;top:472px;width:260px"><svg class="tick"><use href="#tick"/></svg><span>Het verbouwen van je beleggingspand of commercieel vastgoed</span></p>

  <p class="abs back-phone"><svg class="tick" style="width:22px;height:22px"><use href="#phone"/></svg>(088) 415 62 90</p>
  <p class="abs back-url">www.<span class="accent">dovrel</span>.nl</p>

  <div class="abs brand back-brand">Dovrel<span class="brand__dot"></span></div>
</section>

</body>
</html>
```